Bref créative
Complete Stationery Project for KMT
KMT - Real Estate Agency and Education Centre
I need double sided standard sized Business Card [3.5" x 2"]
Fonts and tag lines remain same font. Other texts, we're open to ideas from designers
Simple
Hendra Wiratmo
Owner / Realtor
Wisma Cakra Baruna 11 Floor
Jl. Raya Pemuda Kav. 3-4
Pasir Melati - Kebon Sirih
Jakarta Pusat - 10390
hendrawira@mailbox-example.com
www.hendra-wiratmo-example.com
K98765432
We require 2 different designs for 2 different companies. One is a real estate agency, the other is an education centre which provides courses in real estate, sales, motivation and personal development.
For the real estate agency:
- Name of company is P.T. Kirana Maju Teguh
- logo used shall be without the tagline
- tagline "The Heart of Property" to be placed separately
- we would like to see designs with and without personal photo, as not all agents might be placing their photos.
- Photos should not be in a box
- Name and Cell number needs to be more prominent than other details
- Design should be clean and exudes a branding of professionalism, trustworthiness and respect
For the education centre:
- Name of company is P.T. Sinar Budaya Akademi
- designs will be without photo
- name and cell number need NOT be more prominent
- design should be clean and corporate that exudes a branding of professionalism, reliability and trust
We require designs for:
- Business cards
- Open Top DL Envelopes 110mm x 220mm (plain)
- Open End DL Envelopes 110mm x 220mm (with window)
- Letter head
- Fax Cover
- 2 pocket folder with business card slot
- Open end envelopes 9 ½” x 12 ½”
Colours schemes are important to us to avoid 'clashes' with 'fengshui".
Colours allowed:
- Grey
Colours to be avoided:
- Yellow(and all other earthy colours)
- Green
- Brown(and all other woody colours)
- Red
We are open to ideas, but it should include the logo with tagline
Business card for the agency should also have the words "Buy / Sell / Lease"

```html
<!DOCTYPE html>
<html lang="en">
<head>
<meta charset="utf-8">
<title>KMT – Business Card</title>
<link rel="stylesheet" href="https://fonts.googleapis.com/css2?family=Cabin:wght@400;600;700&display=swap">
<style>
  :root {
    --page-bg: #e9eaec;
    --card-white: #ffffff;
    --blue-deep: #0d3f7a;
    --blue-mid: #1c5fa6;
    --grey-line: #b8bcc2;
    --text-dark: #1d1f22;
    --text-grey: #55595f;
  }
  * { box-sizing: border-box; margin: 0; padding: 0; }
  html, body {
    width: 1200px; height: 780px; overflow: hidden;
    background: var(--page-bg);
    font-family: "Cabin", sans-serif;
  }
  .business-card {
    position: absolute; left: 80px; top: 93px;
    width: 1040px; height: 594px;
    background: var(--card-white);
    border-radius: 30px;
    overflow: hidden;
    box-shadow: 0 10px 30px rgba(0,0,0,0.18);
  }
  .header-band { position: absolute; left: 0; top: 0; width: 1040px; height: 260px; }
  .holder {
    position: absolute; right: 46px; top: 36px;
    text-align: right; color: var(--card-white);
  }
  .holder-name { font-size: 34px; font-weight: 700; letter-spacing: 0.5px; }
  .holder-role { font-size: 24px; font-weight: 600; margin-top: 4px; }
  .holder-services { font-size: 18px; font-weight: 400; margin-top: 6px; letter-spacing: 1px; }
  .brand {
    position: absolute; left: 300px; top: 250px;
    display: flex; align-items: center; gap: 14px;
  }
  .brand-dot { width: 26px; height: 26px; border-radius: 50%; background: var(--blue-mid); }
  .brand-name {
    font-size: 52px; font-weight: 600; color: var(--blue-deep);
    line-height: 1; letter-spacing: 2px;
  }
  .tagline {
    position: absolute; left: 404px; top: 322px;
    font-size: 19px; font-style: italic; color: var(--text-grey);
  }
  .tag-rule {
    position: absolute; left: 330px; top: 362px;
    width: 210px; height: 2px; background: var(--grey-line);
  }
  .address {
    position: absolute; right: 575px; top: 420px;
    text-align: right; font-style: normal;
    font-size: 21px; line-height: 32px; color: var(--text-dark);
  }
  .divider {
    position: absolute; left: 490px; top: 372px;
    width: 2px; height: 200px; background: var(--grey-line);
  }
  .contacts {
    position: absolute; left: 512px; top: 376px;
    list-style: none; font-size: 21px; color: var(--text-dark);
  }
  .contacts li { display: flex; align-items: center; gap: 10px; height: 38px; }
  .contacts li.cell { font-size: 26px; font-weight: 700; color: var(--blue-deep); height: 42px; }
  .contacts svg { width: 22px; height: 22px; fill: currentColor; flex: none; }
</style>
</head>
<body>
  <article class="business-card">
    <svg class="header-band" viewBox="0 0 1040 260" aria-hidden="true">
      <defs>
        <linearGradient id="bandFill" x1="0" y1="0" x2="1" y2="0.4">
          <stop offset="0" stop-color="#0b386d"/>
          <stop offset="0.55" stop-color="#1c5fa6"/>
          <stop offset="1" stop-color="#3d86c9"/>
        </linearGradient>
      </defs>
      <path d="M0 0 H1040 V190 C820 160 520 120 0 200 Z" fill="url(#bandFill)"/>
      <path d="M0 200 C520 120 820 160 1040 190 V215 C820 178 520 150 0 210 Z" fill="#a9adb3"/>
    </svg>

    <div class="holder">
      <p class="holder-name">Hendra Wiratmo</p>
      <p class="holder-role">Owner / Realtor</p>
      <p class="holder-services">Buy / Sell / Lease</p>
    </div>

    <div class="brand">
      <span class="brand-dot"></span>
      <span class="brand-name">KMT</span>
    </div>
    <p class="tagline">The Heart of Property</p>
    <div class="tag-rule"></div>

    <address class="address">
      Wisma Cakra Baruna 11 Floor<br>
      Jl. Raya Pemuda Kav. 3-4<br>
      Pasir Melati - Kebon Sirih<br>
      Jakarta Pusat - 10390
    </address>

    <div class="divider"></div>

    <ul class="contacts">
      <li>
        <svg viewBox="0 0 24 24"><path d="M6.6 10.8a15 15 0 0 0 6.6 6.6l2.2-2.2c.3-.3.7-.4 1-.2 1.1.4 2.3.6 3.6.6.6 0 1 .4 1 1V20c0 .6-.4 1-1 1A17 17 0 0 1 3 4c0-.6.4-1 1-1h3.5c.6 0 1 .4 1 1 0 1.3.2 2.5.6 3.6.1.3 0 .7-.2 1z"/></svg>
        +62 2100 4417
      </li>
      <li class="cell">
        <svg viewBox="0 0 24 24"><path d="M8 1h8a2 2 0 0 1 2 2v18a2 2 0 0 1-2 2H8a2 2 0 0 1-2-2V3a2 2 0 0 1 2-2zm0 3v14h8V4zm4 15.5a1.2 1.2 0 1 0 0 2.4 1.2 1.2 0 0 0 0-2.4z"/></svg>
        +65 8100 2291
      </li>
      <li>
        <svg viewBox="0 0 24 24"><path d="M7 2h9l3 3v5H7zM4 11h16a2 2 0 0 1 2 2v7a2 2 0 0 1-2 2H4a2 2 0 0 1-2-2v-7a2 2 0 0 1 2-2zm3 3v2h4v-2zm7 0v2h2v-2zm0 3v2h2v-2z"/></svg>
        +62 2100 4418
      </li>
      <li>
        <svg viewBox="0 0 24 24"><path d="M12 2a10 10 0 1 0 5 18.7l-1-1.7A8 8 0 1 1 20 12v1a2 2 0 0 1-4 0V7h-2v1a5 5 0 1 0 .8 6.6A4 4 0 0 0 22 13v-1A10 10 0 0 0 12 2zm0 7a3 3 0 1 1 0 6 3 3 0 0 1 0-6z"/></svg>
        hendrawira@mailbox-example.com
      </li>
      <li>
        <svg viewBox="0 0 24 24"><path d="M12 2a10 10 0 1 0 0 20 10 10 0 0 0 0-20zm6.9 9h-3a15 15 0 0 0-1.3-5.6A8 8 0 0 1 18.9 11zM12 4.1c.9 1.2 1.8 3.6 1.9 6.9h-3.8c.1-3.3 1-5.7 1.9-6.9zM9.4 5.4A15 15 0 0 0 8.1 11h-3a8 8 0 0 1 4.3-5.6zM5.1 13h3a15 15 0 0 0 1.3 5.6A8 8 0 0 1 5.1 13zm6.9 6.9c-.9-1.2-1.8-3.6-1.9-6.9h3.8c-.1 3.3-1 5.7-1.9 6.9zm2.6-1.3a15 15 0 0 0 1.3-5.6h3a8 8 0 0 1-4.3 5.6z"/></svg>
        www.hendra-wiratmo-example.com
      </li>
    </ul>
  </article>
</body>
</html>
```